Wix Web design for a Residential redevelopment company

I need a website with a modern and elegant feel that will attract investors. I would like for the color scale to include the colors in our logo and also shades of grey for a modern feel. I need a page for property case studies in which each case study includes property before and after photos, an imbeded youtube video and text in the format of a math problem showing the amount the property was bought for -(minus) what the investor got in return -(minus) rehab costs -(minus) taxes and fees =(equals) Net Profit
However instead of there being an equal sign, I want the math problem to go vertically down with an underline for the equals sign.There needs to be an "About us," page, Investor Inquiries page, Contact Us Page, and Case studies page.
For font formatting, we like Corporate Gothic. Please make the website Wix friendly.

When someone clicks on one of the case study pictures, I would like the pictures to pull up in a click or swipe to the right manner similar to how pictures are structured on brindlo or vexoma.com

Target Market(s)

Investors

Industry/Entity Type

Real Estate

Number of Pages Required

5+ page

Other font styles liked:
• Gothic Corporate

Requirements
Nice to have
• stock photos for the home page

```html
<!DOCTYPE html>
<html lang="en">
<head>
<meta charset="utf-8">
<title>KOVA Property Solutions</title>
<link href="https://fonts.googleapis.com/css2?family=Montserrat:wght@500;600;700;800&family=Didact+Gothic&display=swap" rel="stylesheet">
<style>
:root{
  --green:#6cb51f;
  --green-dark:#3f9a12;
  --blue:#1565c0;
  --ink:#111;
  --text:#333;
  --footer:#1b1b1b;
  --footer-text:#bdbdbd;
  --red:#e3204b;
  --white:#fff;
}
*{box-sizing:border-box;margin:0;padding:0}
html,body{width:1200px;height:2375px;overflow:hidden}
body{position:relative;background:var(--white);font-family:"Didact Gothic",sans-serif;color:var(--text)}
.heading{font-family:"Montserrat",sans-serif}

/* header */
.topbar{position:absolute;left:0;top:0;width:1200px;height:35px;background:linear-gradient(#4caf1a,#2f8f0c);color:#fff;font-size:11px}
.topbar .contact{position:absolute;left:310px;top:11px;display:flex;gap:26px}
.topbar .contact span{display:flex;align-items:center;gap:8px}
.topbar .auth{position:absolute;right:162px;top:8px;display:flex;gap:10px}
.auth a{font-size:9px;padding:3px 7px;color:#fff;text-decoration:none;border:1px solid #fff}
.auth a.signup{background:#fff;color:var(--green-dark)}
.navband{position:absolute;left:0;top:35px;width:1200px;height:79px;background:linear-gradient(90deg,#7cc12a,#6ab322 60%,#89c94a)}
.nav{position:absolute;right:160px;top:32px;display:flex;gap:42px}
.nav a{color:#fff;font-size:12px;text-decoration:none}
.brand{position:absolute;left:161px;top:0;width:127px;height:135px;z-index:3}
.brand svg{position:absolute;inset:0}
.brand .name{position:absolute;left:0;right:0;top:62px;text-align:center;font-family:"Montserrat",sans-serif;font-weight:800;font-size:28px;color:var(--green)}

/* hero */
.hero{position:absolute;left:0;top:114px;width:1200px;height:434px;background:
  radial-gradient(ellipse 420px 300px at 380px 260px,rgba(40,32,26,.55),transparent 70%),
  radial-gradient(ellipse 360px 260px at 1000px 320px,rgba(214,180,70,.55),transparent 70%),
  linear-gradient(100deg,#4e4034 0%,#7d6a56 30%,#b09d86 55%,#c7b088 78%,#6f7f45 100%)}
.hero-frame{position:absolute;left:396px;top:76px;width:408px;height:150px;border:5px solid rgba(255,255,255,.45)}
.hero-title{position:absolute;left:0;right:0;top:115px;text-align:center;color:#fff;font-size:60px;font-weight:700;text-shadow:0 2px 6px rgba(0,0,0,.3)}
.hero-arrow{position:absolute;top:163px;width:54px;height:54px;border:2px solid #fff;background:rgba(0,0,0,.35);display:flex;align-items:center;justify-content:center}
.hero-arrow.prev{left:54px}.hero-arrow.next{left:1089px}
.tabs{position:absolute;left:461px;top:258px;height:48px;display:flex;border-radius:24px;overflow:hidden;border:2px solid #222}
.tabs span{display:flex;align-items:center;justify-content:center;color:#fff;font-family:"Montserrat",sans-serif;font-weight:700;font-size:14px;background:#111;width:87px;border-left:1px solid #444}
.tabs span.on{background:linear-gradient(#8bd23b,#4a9e14);width:90px;border:0}
.tabs span:last-child{width:100px}
.search{position:absolute;left:300px;top:324px;width:602px;height:51px;border-radius:26px;background:#fff;border:3px solid #c9d6e8;display:flex;align-items:center}
.search .field{flex:1;padding-left:20px;color:#777;font-size:15px}
.search .btn{width:150px;height:45px;border-radius:23px;background:var(--blue);color:#fff;font-family:"Montserrat",sans-serif;font-weight:700;font-size:12px;display:flex;align-items:center;justify-content:center}

/* listing sections */
.section-title{position:absolute;left:0;right:0;text-align:center;font-family:"Montserrat",sans-serif;font-weight:700;font-size:25px;color:var(--ink)}
.section-title em{font-style:normal;color:var(--green)}
.section-lead{position:absolute;left:326px;width:548px;text-align:center;font-size:12px;line-height:20px;color:#222}
.slider-arrow{position:absolute;width:30px;height:30px;background:#bdbdbd;display:flex;align-items:center;justify-content:center}
.cards{position:absolute;left:161px;display:flex;gap:22px}
.card{width:204px;height:323px;background:#fff;box-shadow:0 1px 6px rgba(0,0,0,.22);position:relative;overflow:hidden}
.card .photo{height:181px;background:
  linear-gradient(180deg,#c5d3e2 0%,#e6dccb 28%,transparent 30%),
  linear-gradient(90deg,transparent 12%,#8c7a68 12%,#b8aa98 45%,#7a6a58 72%,transparent 72%),
  linear-gradient(180deg,#d9d0c2 0%,#6f8d3c 70%,#4e7a28 100%)}
.card .price{position:absolute;left:0;top:125px;width:116px;height:34px;background:var(--blue);border-radius:0 17px 17px 0;color:#fff;font-size:15px;display:flex;align-items:center;padding-left:13px}
.card .tag{position:absolute;left:15px;top:191px;background:var(--red);color:#fff;font-size:7px;padding:1px 4px;border-radius:2px}
.card .title{position:absolute;left:15px;right:12px;top:205px;font-family:"Montserrat",sans-serif;font-weight:600;font-size:11px;color:var(--ink);white-space:nowrap}
.card .addr{position:absolute;left:15px;top:225px;font-size:10px;line-height:13px;color:#555;padding-left:18px;width:165px}
.card .addr svg{position:absolute;left:0;top:1px}
.card .specs{position:absolute;left:15px;right:18px;top:268px;display:flex;justify-content:space-between;font-size:11px;color:#222}
.card .specs div span{display:block;margin-top:6px;color:var(--blue)}
.view-more{position:absolute;left:537px;width:126px;height:33px;border-radius:17px;background:var(--green);color:#fff;font-family:"Montserrat",sans-serif;font-weight:700;font-size:12px;display:flex;align-items:center;justify-content:center}

/* videos */
.videos{position:absolute;left:0;top:1613px;width:1200px;height:382px;background:linear-gradient(90deg,#eceef0,#e2e6ea)}
.videos .city{position:absolute;left:685px;top:0;width:515px;height:382px;background:linear-gradient(120deg,#e6eaee 0%,#b4c0cd 40%,#7a8a9e 75%,#46556b 100%)}
.videos .section-title{left:161px;right:auto;top:40px;text-align:left}
.video{position:absolute;left:161px;top:84px;width:524px;height:253px;background:
  linear-gradient(90deg,transparent 8%,rgba(90,70,55,.55) 8%,rgba(120,100,80,.5) 50%,transparent 50%,transparent 62%,rgba(110,95,80,.4) 62%,rgba(110,95,80,.4) 78%,transparent 78%) 0 45px/100% 110px no-repeat,
  linear-gradient(#c2ccd5 0%,#b0a795 40%,#6b7a4a 70%,#52683a 100%)}
.play{position:absolute;left:237px;top:95px;width:58px;height:58px;border-radius:50%;background:#fff;display:flex;align-items:center;justify-content:center}
.play-label{position:absolute;left:0;right:0;top:161px;text-align:center;color:#fff;font-family:"Montserrat",sans-serif;font-weight:700;font-size:11px}

/* footer */
.footer{position:absolute;left:0;top:1995px;width:1200px;height:380px;background:var(--footer);color:var(--footer-text)}
.footer .cols{position:absolute;left:161px;top:50px;display:flex}
.footer .col{width:225px}
.footer h4{font-family:"Montserrat",sans-serif;font-weight:700;font-size:12px;color:#fff;margin-bottom:14px}
.footer li{list-style:none;font-size:10px;line-height:24px}
.footer li.more{color:var(--green);font-weight:700}
.footer .rule{position:absolute;left:161px;width:878px;top:237px;border-top:1px solid #333}
.footer .links{position:absolute;left:0;right:0;top:246px;display:flex;justify-content:center;gap:36px;font-size:10px}
.footer .social{position:absolute;left:0;right:0;top:298px;display:flex;justify-content:center;gap:9px}
.footer .social span{width:27px;height:27px;border-radius:50%;background:#8a8a8a}
.footer .copy{position:absolute;left:0;right:0;top:341px;text-align:center;font-size:10px}
</style>
</head>
<body>

<header>
  <div class="topbar">
    <div class="contact">
      <span><svg width="12" height="12" viewBox="0 0 24 24" fill="none" stroke="#fff" stroke-width="2"><path d="M22 16.9v3a2 2 0 0 1-2.2 2 19.8 19.8 0 0 1-8.6-3 19.5 19.5 0 0 1-6-6A19.8 19.8 0 0 1 2.1 4.2 2 2 0 0 1 4.1 2h3a2 2 0 0 1 2 1.7c.1 1 .4 1.9.7 2.8a2 2 0 0 1-.5 2.1L8 9.9a16 16 0 0 0 6 6l1.3-1.3a2 2 0 0 1 2.1-.4c.9.3 1.8.6 2.8.7a2 2 0 0 1 1.7 2z"/></svg>+1 (555) 01234 5678</span>
      <span><svg width="13" height="11" viewBox="0 0 24 20" fill="none" stroke="#fff" stroke-width="2"><rect x="1" y="1" width="22" height="18"/><path d="M1 1l11 9 11-9"/></svg>hello@kovaproperty.com</span>
    </div>
    <div class="auth"><a href="#">Log In</a><a href="#" class="signup">Sign Up</a></div>
  </div>
  <div class="navband">
    <nav class="nav"><a href="#">Home</a><a href="#">About Us</a><a href="#">Investor Inquiries</a><a href="#">Case Studies</a><a href="#">Contact Us</a></nav>
  </div>
  <div class="brand">
    <svg width="127" height="135" viewBox="0 0 127 135"><path d="M0 0H127V115L63.5 135 0 115Z" fill="#fff"/></svg>
    <div class="name">KOVA</div>
  </div>
</header>

<section class="hero" role="img" aria-label="Young couple reviewing home documents with an agent in a bright living room">
  <div class="hero-frame"></div>
  <h1 class="hero-title heading">Find Your Way Home</h1>
  <div class="hero-arrow prev"><svg width="12" height="12" viewBox="0 0 12 12"><path d="M8 1L3 6l5 5" stroke="#fff" stroke-width="2.5" fill="none"/></svg></div>
  <div class="hero-arrow next"><svg width="12" height="12" viewBox="0 0 12 12"><path d="M4 1l5 5-5 5" stroke="#fff" stroke-width="2.5" fill="none"/></svg></div>
  <div class="tabs"><span class="on">BUY</span><span>RENT</span><span>SALE</span></div>
  <div class="search"><div class="field">New York, NY</div><div class="btn">SEARCH</div></div>
</section>

<h2 class="section-title" style="top:583px"><em>LATEST</em> PROPERTIES</h2>
<p class="section-lead" style="top:616px">Lorem ipsum dolor sit amet, consectetur adipisicing elit, sed do eiusmod tempor incididunt ut labore et dolore magna aliqua. Ut enim ad minim</p>
<div class="slider-arrow" style="left:105px;top:807px"><svg width="10" height="10" viewBox="0 0 10 10"><path d="M7 1L3 5l4 4" stroke="#fff" stroke-width="2" fill="none"/></svg></div>
<div class="slider-arrow" style="left:1065px;top:807px"><svg width="10" height="10" viewBox="0 0 10 10"><path d="M3 1l4 4-4 4" stroke="#fff" stroke-width="2" fill="none"/></svg></div>
<div class="cards" style="top:674px">
  <article class="card"><div class="photo" role="img" aria-label="Modern apartment building with landscaped grounds"></div><div class="price">$1,750,000</div><span class="tag">SALE</span><h3 class="title">Nemo enim ipsam voluptatem</h3><p class="addr"><svg width="9" height="12" viewBox="0 0 9 12"><path d="M4.5 0A4.5 4.5 0 0 0 0 4.5C0 8 4.5 12 4.5 12S9 8 9 4.5A4.5 4.5 0 0 0 4.5 0zm0 6.2a1.7 1.7 0 1 1 0-3.4 1.7 1.7 0 0 1 0 3.4z" fill="#888"/></svg>42, Alder Court, New York, NY2154215</p><div class="specs"><div>Bedrooms<span>02</span></div><div>Baths<span>02</span></div><div>Size (Sq.ft)<span>1999</span></div></div></article>
  <article class="card"><div class="photo" role="img" aria-label="Modern apartment building with landscaped grounds"></div><div class="price">$1,750,000</div><span class="tag">SALE</span><h3 class="title">Nemo enim ipsam voluptatem</h3><p class="addr"><svg width="9" height="12" viewBox="0 0 9 12"><path d="M4.5 0A4.5 4.5 0 0 0 0 4.5C0 8 4.5 12 4.5 12S9 8 9 4.5A4.5 4.5 0 0 0 4.5 0zm0 6.2a1.7 1.7 0 1 1 0-3.4 1.7 1.7 0 0 1 0 3.4z" fill="#888"/></svg>42, Alder Court, New York, NY2154215</p><div class="specs"><div>Bedrooms<span>02</span></div><div>Baths<span>02</span></div><div>Size (Sq.ft)<span>1999</span></div></div></article>
  <article class="card"><div class="photo" role="img" aria-label="Modern apartment building with landscaped grounds"></div><div class="price">$1,750,000</div><span class="tag">SALE</span><h3 class="title">Nemo enim ipsam voluptatem</h3><p class="addr"><svg width="9" height="12" viewBox="0 0 9 12"><path d="M4.5 0A4.5 4.5 0 0 0 0 4.5C0 8 4.5 12 4.5 12S9 8 9 4.5A4.5 4.5 0 0 0 4.5 0zm0 6.2a1.7 1.7 0 1 1 0-3.4 1.7 1.7 0 0 1 0 3.4z" fill="#888"/></svg>42, Alder Court, New York, NY2154215</p><div class="specs"><div>Bedrooms<span>02</span></div><div>Baths<span>02</span></div><div>Size (Sq.ft)<span>1999</span></div></div></article>
  <article class="card"><div class="photo" role="img" aria-label="Modern apartment building with landscaped grounds"></div><div class="price">$1,750,000</div><span class="tag">SALE</span><h3 class="title">Nemo enim ipsam voluptatem</h3><p class="addr"><svg width="9" height="12" viewBox="0 0 9 12"><path d="M4.5 0A4.5 4.5 0 0 0 0 4.5C0 8 4.5 12 4.5 12S9 8 9 4.5A4.5 4.5 0 0 0 4.5 0zm0 6.2a1.7 1.7 0 1 1 0-3.4 1.7 1.7 0 0 1 0 3.4z" fill="#888"/></svg>42, Alder Court, New York, NY2154215</p><div class="specs"><div>Bedrooms<span>02</span></div><div>Baths<span>02</span></div><div>Size (Sq.ft)<span>1999</span></div></div></article>
</div>
<a class="view-more" style="top:1026px">VIEW MORE</a>

<h2 class="section-title" style="top:1090px"><em>SAFE</em> NEIGHBORHOODS</h2>
<p class="section-lead" style="top:1123px">Lorem ipsum dolor sit amet, consectetur adipisicing elit, sed do eiusmod tempor incididunt ut labore et dolore magna aliqua. Ut enim ad minim</p>
<div class="slider-arrow" style="left:105px;top:1314px"><svg width="10" height="10" viewBox="0 0 10 10"><path d="M7 1L3 5l4 4" stroke="#fff" stroke-width="2" fill="none"/></svg></div>
<div class="slider-arrow" style="left:1065px;top:1314px"><svg width="10" height="10" viewBox="0 0 10 10"><path d="M3 1l4 4-4 4" stroke="#fff" stroke-width="2" fill="none"/></svg></div>
<div class="cards" style="top:1181px">
  <article class="card"><div class="photo" role="img" aria-label="Modern apartment building with landscaped grounds"></div><div class="price">$1,750,000</div><span class="tag">SALE</span><h3 class="title">Nemo enim ipsam voluptatem</h3><p class="addr"><svg width="9" height="12" viewBox="0 0 9 12"><path d="M4.5 0A4.5 4.5 0 0 0 0 4.5C0 8 4.5 12 4.5 12S9 8 9 4.5A4.5 4.5 0 0 0 4.5 0zm0 6.2a1.7 1.7 0 1 1 0-3.4 1.7 1.7 0 0 1 0 3.4z" fill="#888"/></svg>42, Alder Court, New York, NY2154215</p><div class="specs"><div>Bedrooms<span>02</span></div><div>Baths<span>02</span></div><div>Size (Sq.ft)<span>1999</span></div></div></article>
  <article class="card"><div class="photo" role="img" aria-label="Modern apartment building with landscaped grounds"></div><div class="price">$1,750,000</div><span class="tag">SALE</span><h3 class="title">Nemo enim ipsam voluptatem</h3><p class="addr"><svg width="9" height="12" viewBox="0 0 9 12"><path d="M4.5 0A4.5 4.5 0 0 0 0 4.5C0 8 4.5 12 4.5 12S9 8 9 4.5A4.5 4.5 0 0 0 4.5 0zm0 6.2a1.7 1.7 0 1 1 0-3.4 1.7 1.7 0 0 1 0 3.4z" fill="#888"/></svg>42, Alder Court, New York, NY2154215</p><div class="specs"><div>Bedrooms<span>02</span></div><div>Baths<span>02</span></div><div>Size (Sq.ft)<span>1999</span></div></div></article>
  <article class="card"><div class="photo" role="img" aria-label="Modern apartment building with landscaped grounds"></div><div class="price">$1,750,000</div><span class="tag">SALE</span><h3 class="title">Nemo enim ipsam voluptatem</h3><p class="addr"><svg width="9" height="12" viewBox="0 0 9 12"><path d="M4.5 0A4.5 4.5 0 0 0 0 4.5C0 8 4.5 12 4.5 12S9 8 9 4.5A4.5 4.5 0 0 0 4.5 0zm0 6.2a1.7 1.7 0 1 1 0-3.4 1.7 1.7 0 0 1 0 3.4z" fill="#888"/></svg>42, Alder Court, New York, NY2154215</p><div class="specs"><div>Bedrooms<span>02</span></div><div>Baths<span>02</span></div><div>Size (Sq.ft)<span>1999</span></div></div></article>
  <article class="card"><div class="photo" role="img" aria-label="Modern apartment building with landscaped grounds"></div><div class="price">$1,750,000</div><span class="tag">SALE</span><h3 class="title">Nemo enim ipsam voluptatem</h3><p class="addr"><svg width="9" height="12" viewBox="0 0 9 12"><path d="M4.5 0A4.5 4.5 0 0 0 0 4.5C0 8 4.5 12 4.5 12S9 8 9 4.5A4.5 4.5 0 0 0 4.5 0zm0 6.2a1.7 1.7 0 1 1 0-3.4 1.7 1.7 0 0 1 0 3.4z" fill="#888"/></svg>42, Alder Court, New York, NY2154215</p><div class="specs"><div>Bedrooms<span>02</span></div><div>Baths<span>02</span></div><div>Size (Sq.ft)<span>1999</span></div></div></article>
</div>
<a class="view-more" style="top:1536px">VIEW MORE</a>

<section class="videos">
  <div class="city" role="img" aria-label="Businessman using a tablet with a city skyline overlay"></div>
  <h2 class="section-title"><em>KOVA</em> VIDEOS</h2>
  <div class="video" role="img" aria-label="Video still of a modern residential complex beside a pond">
    <div class="play"><svg width="18" height="20" viewBox="0 0 18 20"><path d="M2 1l15 9-15 9z" fill="#222"/></svg></div>
    <div class="play-label">PLAY VIDEO</div>
  </div>
</section>

<footer class="footer">
  <div class="cols">
    <div class="col"><h4>REAL ESTATE MARKETS</h4><ul><li>Alabama Real Estate</li><li>Alaska Real Estate</li><li>Arizona Real Estate</li><li>Arkansas Real Estate</li><li class="more">More</li></ul></div>
    <div class="col"><h4>RENTAL MARKETS</h4><ul><li>Alabama Rentals</li><li>Alaska Rentals</li><li>Arizona Rentals</li><li>Arkansas Rentals</li><li class="more">More</li></ul></div>
    <div class="col"><h4>BROWSE HOMES</h4><ul><li>California</li><li>Texas</li><li>New York</li><li>Florida</li><li class="more">More</li></ul></div>
    <div class="col"><h4>FOR PROFESSIONALS</h4><ul><li>Stats &amp; Trends</li><li>Home Price Maps</li><li>U.S. Property Records</li><li>Popular Counties</li><li class="more">More</li></ul></div>
  </div>
  <div class="rule"></div>
  <nav class="links"><span>Home</span><span>About Us</span><span>Investor Inquiries</span><span>Case Studies</span><span>Contact Us</span></nav>
  <div class="social" aria-label="Social links"><span></span><span></span><span></span></div>
  <p class="copy">Copyright © 2018 KOVA Property Solutions. All rights reserved.</p>
</footer>

</body>
</html>
```